Design a New Business Card for Our Company

We are looking for fresh, unique, and a modern business card that reflects our roots as digital marketing agency focused on SEM.

Industry/Entity Type

Marketing

Contact Information for Business Card

looking for very unique out of the box designs. clean and modern that compliments our logo

Requirements
Must have
• colors should match our logo
• Front should have name, address, email, and phone/fax of the person, phone/fax are the same number
• back should have our url

```html
<!DOCTYPE html>
<html lang="en">
<head>
<meta charset="utf-8">
<title>Brightpath Business Card</title>
<link rel="stylesheet" href="https://fonts.googleapis.com/css2?family=Open+Sans:wght@400;600;700&display=swap">
<style>
  :root {
    --backdrop: #3a3a3a;
    --card-white: #ffffff;
    --brand-blue: #5f97d1;
    --brand-grey: #a9a9a9;
    --band-grey: #b5b5b5;
    --text-dark: #4a4a4a;
    --divider: #cfcfcf;
  }
  * { margin: 0; padding: 0; box-sizing: border-box; }
  html, body {
    width: 1105px;
    height: 1200px;
    overflow: hidden;
    background: var(--backdrop);
    font-family: "Open Sans", Arial, sans-serif;
  }
  .card {
    position: absolute;
    left: 196px;
    width: 720px;
  }
  .card--front {
    top: 146px;
    height: 412px;
    background: var(--card-white);
  }
  .card--back {
    top: 602px;
    height: 410px;
    background: var(--brand-blue);
  }
  .brand {
    position: absolute;
    left: 0;
    right: 0;
    top: 66px;
    display: flex;
    justify-content: center;
    align-items: center;
    gap: 14px;
  }
  .brand__dot {
    width: 38px;
    height: 38px;
    border-radius: 50%;
    background: var(--brand-blue);
  }
  .brand__name {
    font-size: 60px;
    font-weight: 700;
    line-height: 1;
    letter-spacing: -1px;
    color: var(--brand-grey);
  }
  .person {
    position: absolute;
    right: 426px;
    top: 240px;
    text-align: right;
  }
  .person__name {
    font-size: 25px;
    font-weight: 600;
    color: var(--brand-grey);
    line-height: 1.2;
  }
  .person__role {
    font-size: 19px;
    color: var(--brand-blue);
    line-height: 1.3;
  }
  .divider {
    position: absolute;
    left: 319px;
    top: 199px;
    width: 1px;
    height: 145px;
    background: var(--divider);
  }
  .contact {
    position: absolute;
    left: 342px;
    top: 200px;
    font-size: 18.5px;
    color: var(--text-dark);
    line-height: 25px;
    list-style: none;
  }
  .contact__address { margin-bottom: 8px; }
  .contact__line {
    display: flex;
    align-items: center;
    gap: 10px;
    height: 28px;
  }
  .contact__icon { width: 18px; height: 18px; fill: #8a8a8a; flex: none; }
  .band {
    position: absolute;
    left: 0;
    bottom: 0;
    width: 720px;
    height: 28px;
    display: block;
  }
  .back-brand {
    position: absolute;
    left: 0;
    right: 0;
    top: 168px;
    text-align: center;
    font-size: 64px;
    font-weight: 700;
    letter-spacing: -1px;
    color: var(--card-white);
    line-height: 1;
  }
  .back-url {
    position: absolute;
    left: 0;
    right: 0;
    top: 346px;
    text-align: center;
    font-size: 18px;
    letter-spacing: 4px;
    color: var(--card-white);
  }
</style>
</head>
<body>
  <section class="card card--front">
    <div class="brand">
      <span class="brand__dot"></span>
      <span class="brand__name">brightpath</span>
    </div>

    <div class="person">
      <p class="person__name">Daniel Reyes</p>
      <p class="person__role">CEO/Founder</p>
    </div>

    <div class="divider"></div>

    <ul class="contact">
      <li class="contact__address">2140 Willow Creek Road<br>Denver, Colorado 80211</li>
      <li class="contact__line">
        <svg class="contact__icon" viewBox="0 0 24 24" aria-hidden="true"><path d="M6.6 10.8a15.1 15.1 0 0 0 6.6 6.6l2.2-2.2a1 1 0 0 1 1-.25 11.4 11.4 0 0 0 3.6.57 1 1 0 0 1 1 1V20a1 1 0 0 1-1 1A17 17 0 0 1 3 4a1 1 0 0 1 1-1h3.5a1 1 0 0 1 1 1c0 1.25.2 2.45.57 3.57a1 1 0 0 1-.25 1z"/></svg>
        <span>555 210 4836</span>
      </li>
      <li class="contact__line">
        <svg class="contact__icon" viewBox="0 0 24 24" aria-hidden="true"><path d="M6 2h10l2 2v5H6z M3 10h18a1 1 0 0 1 1 1v8a1 1 0 0 1-1 1H3a1 1 0 0 1-1-1v-8a1 1 0 0 1 1-1z M6 14h12v2H6z"/></svg>
        <span>555 390 7125</span>
      </li>
      <li class="contact__line">
        <svg class="contact__icon" viewBox="0 0 24 24" aria-hidden="true"><path d="M2 5h20v14H2z M3 6l9 7 9-7" fill="#8a8a8a"/><path d="M3.5 6.5l8.5 6.5 8.5-6.5" fill="none" stroke="#fff" stroke-width="1.5"/></svg>
        <span>dan@brightpath.com</span>
      </li>
    </ul>

    <svg class="band" viewBox="0 0 720 28" aria-hidden="true">
      <polygon points="0,0 470,0 463,28 0,28" fill="var(--band-grey)"/>
      <polygon points="477,0 720,0 720,28 470,28" fill="var(--brand-blue)"/>
    </svg>
  </section>

  <section class="card card--back">
    <p class="back-brand">brightpath</p>
    <p class="back-url">www.brightpath.com</p>
  </section>
</body>
</html>
```